Wandkalender Herrliches Talbergen
Zielgruppe
Souvenir- und Geschenkartiekl aus Ratzeburg
Aufgabenstellung
· Gesucht wird eine Designvorlage für die Gestaltung eines Jahreswandkalenders mit Naturfotos aus der Inselstadt Ratzeburg.
· Es muss nur ein Titelblatt und ein Monatsblatt gestaltet werden, die restlichen 11 Monate würden wir adaptieren.
· Das Format des Kalenders beträgt 50 x 70 cm im Hochformat
· Das Monatslayout soll Bilder im Hoch- und im Querformat zulassen
· Als Anlage habe ich einen ersten Entwurf von uns gepackt, der mir aber zu unoriginell bzw. zu konventionell ist.
· Die Zielgruppe ist tendenziell die Generation 50+

```html
<!DOCTYPE html>
<html lang="de">
<head>
<meta charset="utf-8">
<title>Wandkalender Herrliches Talbergen – Juli 2017</title>
<link rel="stylesheet" href="https://fonts.googleapis.com/css2?family=Great+Vibes&family=Ubuntu:wght@400;500;700&display=swap">
<style>
  :root {
    --page: #ffffff;
    --frame-cream: #fbf5df;
    --frame-edge: #efe6c4;
    --ink: #111111;
    --muted: #a9a9a9;
    --accent-red: #c0141f;
    --rule: #6e6e6e;
  }
  * { box-sizing: border-box; margin: 0; padding: 0; }
  html, body { width: 848px; height: 1200px; overflow: hidden; }
  body {
    position: relative;
    background: var(--page);
    font-family: "Ubuntu", sans-serif;
    color: var(--ink);
  }

  /* Photo frame */
  .photo-mat {
    position: absolute;
    left: 30px; top: 80px; width: 599px; height: 755px;
    background: var(--frame-cream);
    border: 3px dotted var(--frame-edge);
    box-shadow: 0 2px 6px rgba(120, 110, 70, 0.18);
  }
  .photo-card {
    position: absolute;
    left: 57px; top: 110px; width: 541px; height: 689px;
    background: var(--page);
    border-radius: 8px;
  }
  .photo-slot {
    position: absolute;
    left: 70px; top: 125px; width: 513px; height: 660px;
    background: linear-gradient(180deg,
      #d8dcdf 0%, #d8dcdf 11%,
      #c8683d 18%, #b5573a 28%,
      #8b3f2f 33%, #4f7c34 45%,
      #3d6e2b 70%, #b9573f 87%,
      #8c8b86 100%);
  }

  /* Notes column */
  .notes-title {
    position: absolute;
    left: 650px; top: 80px; width: 165px;
    text-align: center;
    font-family: "Great Vibes", cursive;
    font-size: 52px;
    line-height: 1;
    color: var(--accent-red);
  }
  .notes-lines {
    position: absolute;
    left: 645px; top: 195px; width: 169px;
    list-style: none;
  }
  .notes-lines li {
    height: 37.9px;
    border-top: 1px solid var(--rule);
  }

  /* Month grid */
  .month-grid {
    position: absolute;
    left: 67px; top: 870px;
    display: grid;
    grid-template-columns: 38px 52px 45px 48px 51px 45px 48px 48px;
    grid-auto-rows: 32.2px;
    font-size: 24px;
    font-weight: 500;
    line-height: 32px;
  }
  .month-grid span { text-align: right; }
  .month-grid .week { text-align: left; color: var(--muted); font-weight: 400; }
  .month-grid .sat { color: var(--muted); font-weight: 400; }
  .month-grid .sun { color: var(--accent-red); }

  .footer-caption {
    position: absolute;
    left: 67px; top: 1128px;
    font-size: 11px;
    color: var(--muted);
    letter-spacing: 0.2px;
  }

  /* Month title */
  .month-name {
    position: absolute;
    left: 470px; top: 858px;
    font-family: "Great Vibes", cursive;
    font-size: 188px;
    line-height: 1;
    white-space: nowrap;
    color: var(--accent-red);
  }
  .year {
    position: absolute;
    left: 638px; top: 1028px;
    font-size: 62px;
    font-weight: 700;
    line-height: 1;
    color: var(--ink);
  }
</style>
</head>
<body>
  <div class="photo-mat"></div>
  <div class="photo-card"></div>
  <div class="photo-slot" role="img" aria-label="Foto: Backsteinhaus mit rotem Ziegeldach, Fassade von roten und weißen Kletterrosen bewachsen"></div>

  <div class="notes-title">Notizen</div>
  <ul class="notes-lines">
    <li></li><li></li><li></li><li></li><li></li><li></li><li></li><li></li>
    <li></li><li></li><li></li><li></li><li></li><li></li><li></li><li></li>
  </ul>

  <div class="month-grid">
    <span class="week">KW</span><span>Mo</span><span>Di</span><span>Mi</span><span>Do</span><span>Fr</span><span class="sat">Sa</span><span class="sun">So</span>
    <span class="week">26</span><span></span><span></span><span></span><span></span><span></span><span class="sat">1</span><span class="sun">2</span>
    <span class="week">27</span><span>3</span><span>4</span><span>5</span><span>6</span><span>7</span><span class="sat">8</span><span class="sun">9</span>
    <span class="week">28</span><span>10</span><span>11</span><span>12</span><span>13</span><span>14</span><span class="sat">15</span><span class="sun">16</span>
    <span class="week">29</span><span>17</span><span>18</span><span>19</span><span>20</span><span>21</span><span class="sat">22</span><span class="sun">23</span>
    <span class="week">30</span><span>24</span><span>25</span><span>26</span><span>27</span><span>28</span><span class="sat">29</span><span class="sun">30</span>
    <span class="week">31</span><span>31</span>
  </div>

  <p class="footer-caption">Mein herrliches Talbergen</p>

  <div class="month-name">Juli</div>
  <div class="year">2017</div>
</body>
</html>
```